Nine Lanterns Quill House Book Cover for: "Growing Older Wisely"

We are a publishing company who plans to launch the book, Growing Older Wisely, A Handy Compact Manual for Legal, Financial and Emotional Health in late 2018. We desire a book cover that creates interest, looks professional and can draw readers to open and purchase this book. Growing Older Wisely is an invaluable, self-help book which provides Generation X, Baby Boomers and their families with the following information: steps to obtain valid, reliable wills and trusts, identify and pay for health care, address end of life care and manage grief. (Please see the attached book description for more information about the book contents). The cover needs to have a "wellness", health and healing emphasis but it should not be morbid. Instead, the cover should have an uplifting, inviting and engaging feeling.

The designer should use Photoshop to develop the 5 x 7 cover. Please design the front, back cover and spine using the attached suggested layout as a guide. Use colors that complement the background colors in the author's photo and the logo for the front and back colors. Feel free to change the colors of the black rectangles on the front of the book. We are looking for a design to be added using the suggested layouts but we are open to modifications of the layout provided that all the content in the attachments are used. Below are the specifications needed for the cover:

-Use Photoshop
-Develop a front and back cover for a 5 x 7 format book
-Include the book title, subtitle and author name on the front cover as noted on the front cover attachment
-Include a book title and author names on the spine of the cover
-Use full bleed background if appropriate
-Color correct and resize images as necessary
-Insert logo and publisher’s imprint on spine and back cover as noted in attachments

For designers who are successful with this contest, we will primarily consider you for future projects.

Thanks!

Target Market(s)

Generation X, Baby Boomers and their families

Industry/Entity Type

Book Publisher

Font styles to use
Sans Serif

Colors

Designer to choose colors to be used in the design.

Requirements
Must have
• The designer should use Photoshop to develop the 5 x 7 cover. Please design the front, back cover and spine using the attached suggested layout as a guide. Use colors that complement the background colors in the author's photo and the logo for the front and back colors. Feel free to change the colors of the black rectangles on the front of the book. We are looking for a design to be added using the suggested layouts but we are open to modifications of the layout provided that all the content in the attachments are used. Below are the specifications needed for the cover:
• -Use Photoshop
• -Develop a front and back cover for a 5 x 7 format book
• -Include the book title, subtitle and author name on the front cover as noted on the front cover attachment
• -Include a book title and author names on the spine of the cover
• -Use full bleed background if appropriate
• -Color correct and resize images as necessary
• -Insert logo and publisher’s imprint on spine and back cover as noted in attachments
Nice to have
• N/A
Should not have
• The design should not specifically duplicate the layout samples or include pictures of persons on the cover. We have provided those as a guide; we are looking for innovation and professionalism.

```html
<!DOCTYPE html>
<html lang="en">
<head>
<meta charset="utf-8">
<title>Growing Older Wisely — Cover</title>
<link href="https://fonts.googleapis.com/css2?family=EB+Garamond:ital,wght@0,400;0,500;1,400&display=swap" rel="stylesheet">
<style>
  :root {
    --page-bg: #ffffff;
    --spine-green: #7fcf5c;
    --ink: #1c140f;
    --canopy-light: #fbfbe6;
    --canopy-mid: #d4e979;
    --canopy-deep: #7cc043;
    --canopy-edge: #5ea536;
  }
  * { margin: 0; padding: 0; box-sizing: border-box; }
  html, body {
    width: 1200px; height: 1200px; overflow: hidden;
    background: var(--page-bg);
    font-family: "EB Garamond", Georgia, serif;
    color: var(--ink);
  }
  .book {
    position: absolute; left: 203px; top: 100px;
    width: 794px; height: 1000px; display: flex;
  }
  .spine {
    width: 90px; height: 100%; flex: none;
    background: var(--spine-green);
    position: relative; overflow: hidden;
  }
  .spine-title, .spine-subtitle {
    position: absolute; top: 40px;
    writing-mode: vertical-rl;
    white-space: nowrap; line-height: 1;
  }
  .spine-title { right: 28px; font-size: 44px; letter-spacing: 1px; }
  .spine-subtitle { right: 10px; font-size: 14.5px; }
  .spine-authors {
    position: absolute; top: 720px; left: 0; right: 0;
    text-align: center;
    font-size: 13px; line-height: 1.7; text-transform: uppercase;
    white-space: nowrap;
  }
  .spine-authors .joiner { text-transform: none; }
  .spine-imprint {
    position: absolute; top: 850px; bottom: 20px; left: 0; right: 0;
    display: flex; flex-direction: column; align-items: center; gap: 8px;
  }
  .imprint-mark { width: 16px; height: 16px; background: var(--ink); flex: none; }
  .imprint-name {
    writing-mode: vertical-rl; white-space: nowrap;
    font-size: 10px; line-height: 1;
  }
  .front {
    width: 704px; height: 100%; position: relative; overflow: hidden; flex: none;
  }
  .canopy {
    position: absolute; inset: 0;
    background:
      radial-gradient(ellipse 55% 50% at 48% 52%, var(--canopy-light) 0%, var(--canopy-mid) 45%, transparent 75%),
      radial-gradient(ellipse 90% 80% at 50% 45%, var(--canopy-mid) 0%, var(--canopy-deep) 60%, var(--canopy-edge) 100%);
  }
  .front-content { position: absolute; inset: 0; }
  .praise {
    position: absolute; top: 52px; left: 225px;
    font-size: 40px; line-height: 1; transform: rotate(3deg);
  }
  .praise-source {
    position: absolute; top: 112px; left: 305px;
    font-size: 19px; font-style: italic; transform: rotate(3deg);
  }
  .title-word { position: absolute; line-height: 1; font-weight: 400; }
  .title-growing { top: 330px; left: 110px; font-size: 150px; }
  .title-older { top: 480px; left: 410px; font-size: 56px; }
  .title-wisely { top: 520px; left: 130px; font-size: 150px; }
  .subtitle {
    position: absolute; top: 700px; left: 0; right: 0;
    text-align: center; font-size: 27px; line-height: 1.45;
  }
  .authors {
    position: absolute; top: 895px; left: 0; right: 0;
    text-align: center; font-size: 20px; letter-spacing: 0.3px;
    text-transform: uppercase; white-space: nowrap;
  }
  .authors .joiner { text-transform: none; }
</style>
</head>
<body>
  <div class="book">
    <div class="spine">
      <span class="spine-title">Growing Older Wisely</span>
      <span class="spine-subtitle">A Handy Compact Manual for Legal, Financial and Emotional Health</span>
      <div class="spine-authors">
        Holloway<br><span class="joiner">with</span><br>Abernathy
      </div>
      <div class="spine-imprint">
        <span class="imprint-mark"></span>
        <span class="imprint-name">Nine Lanterns Quill House</span>
      </div>
    </div>
    <div class="front">
      <div class="canopy" role="img" aria-label="Sunlit canopy of tall green trees seen from below, light bursting through the leaves"></div>
      <div class="front-content">
        <p class="praise">“Indispensable!”</p>
        <p class="praise-source">—The Riverbend Courier</p>
        <h1>
          <span class="title-word title-growing">Growing</span>
          <span class="title-word title-older">Older</span>
          <span class="title-word title-wisely">Wisely</span>
        </h1>
        <p class="subtitle">A Handy Compact Manual<br>for Legal, Financial and Emotional Health</p>
        <p class="authors">Maren T. Holloway, M.P.A. <span class="joiner">with</span> Desmond R. Abernathy, Esq.</p>
      </div>
    </div>
  </div>
</body>
</html>
```